依頼詳細
医院の役員の名刺を新しくしたいと思っております。
ピンクを基調としたシンプルなデザインでお願いします。
当院のロゴも入れて頂きたいです。
記載項目
表面 会社名・役職・氏名・住所・電話・FAX・mail
裏面 理事長のみ裏面は英語 その他は白紙で大丈夫です。
希望イメージ
シンプル 複雑
単色 カラフル
暗い 明るい
日常 高級
遊び心 厳粛
未来的 伝統的
女性的 男性的
希望する色
赤系
納品ファイル
補足説明
■ 選んだ理由

ピンクを基調としたグラデーションがきれいで、かつスッキリしたデザインが気に入りました。また実際に使われる先生方にも気に入ってもらえたのでこちらの提案を選ばせていただきました。

■ 提案者全員のお礼・コメント

提案してくださったみなさん、たくさんのご提案ありがとうございました。
とても素敵な提案ばかりで悩みましたが、こちらに決定させていただきました。

また依頼することもあるかと思いますので、今後ともよろしくお願い致します。
本当にありがとうございました。

```html
<!DOCTYPE html>
<html lang="ja">
<head>
<meta charset="utf-8">
<title>桜井歯科クリニック 名刺</title>
<link href="https://fonts.googleapis.com/css2?family=Noto+Sans+JP:wght@400;500&family=Noto+Serif+JP:wght@400;500&display=swap" rel="stylesheet">
<style>
  :root {
    --page: #f3f2ef;
    --card: #ffffff;
    --pink: #e8779e;
    --pink-soft: #f3b6cb;
    --pink-pale: #fbe6ee;
    --ink: #333333;
    --muted: #555555;
    --rule: #d9d9d9;
  }
  * { box-sizing: border-box; margin: 0; padding: 0; }
  html, body { width: 843px; height: 1200px; overflow: hidden; }
  body {
    background: var(--page);
    font-family: "Noto Sans JP", sans-serif;
    color: var(--ink);
    position: relative;
  }
  .card {
    position: absolute;
    left: 72px;
    width: 700px;
    height: 423px;
    background: var(--card);
    overflow: hidden;
  }
  .card--front { top: 150px; }
  .card--back  { top: 640px; }

  .brand { position: absolute; left: 38px; top: 32px; display: flex; align-items: center; gap: 16px; }
  .brand__mark { width: 62px; height: 62px; border-radius: 50%; background: var(--pink); flex: none; }
  .brand__org { font-size: 17px; color: var(--pink); letter-spacing: 0.06em; line-height: 1.3; }
  .brand__name { font-size: 27px; color: var(--pink); letter-spacing: 0.05em; line-height: 1.3; }
  .brand__name--en { font-size: 26px; letter-spacing: 0.04em; }

  .person { position: absolute; display: flex; align-items: baseline; }
  .card--front .person { right: 52px; top: 188px; }
  .person__title { font-size: 13px; color: var(--muted); margin-right: 14px; }
  .person__name { font-family: "Noto Serif JP", serif; font-size: 36px; letter-spacing: 0.12em; font-weight: 500; }
  .person__romaji { position: absolute; right: 52px; top: 245px; font-family: "Noto Serif JP", serif; font-size: 13px; color: var(--muted); letter-spacing: 0.04em; }

  .contact { position: absolute; font-size: 13.5px; line-height: 1.75; color: var(--muted); }
  .card--front .contact { right: 52px; top: 278px; text-align: right; }
  .contact__mail { margin-top: 2px; }

  .card--back .person { left: 230px; top: 198px; }
  .card--back .person__title { font-family: "Noto Sans JP", sans-serif; font-size: 14px; margin-right: 28px; }
  .card--back .person__name { font-size: 38px; letter-spacing: 0.06em; }
  .card--back .contact { left: 230px; top: 286px; font-size: 13px; }

  .band {
    position: absolute; left: 0; right: 0; bottom: 0; height: 48px;
    background: linear-gradient(90deg, var(--card) 0%, var(--pink-pale) 35%, var(--pink-soft) 75%, var(--pink) 100%);
  }
  .band::after {
    content: ""; position: absolute; left: 0; right: 0; bottom: 0; height: 10px;
    background: linear-gradient(90deg, #ffffff 0%, #ececec 60%, var(--rule) 100%);
  }
</style>
</head>
<body>

  <section class="card card--front" aria-label="名刺 表面">
    <header class="brand">
      <span class="brand__mark"></span>
      <div>
        <p class="brand__org">医療法人 和光会</p>
        <p class="brand__name">桜井歯科クリニック</p>
      </div>
    </header>
    <div class="person">
      <span class="person__title">理事長</span>
      <span class="person__name">桜井 健一</span>
    </div>
    <p class="person__romaji">Kenichi Sakurai</p>
    <address class="contact" style="font-style:normal">
      <p>〒530-0001 大阪府大阪市北区梅田1-2-3 サクラビル1F</p>
      <p>Tel.06-1234-5678　Fax.06-1234-5679</p>
      <p class="contact__mail">e-mail : info@sakurai-dc.example</p>
    </address>
    <div class="band"></div>
  </section>

  <section class="card card--back" aria-label="名刺 裏面">
    <header class="brand">
      <span class="brand__mark"></span>
      <p class="brand__name brand__name--en">SAKURAI DENTAL CLINIC</p>
    </header>
    <div class="person">
      <span class="person__title">president</span>
      <span class="person__name">Kenichi　Sakurai</span>
    </div>
    <address class="contact" style="font-style:normal">
      <p>Sakura Bldg 1F,1-2-3,Umeda,Kita-ku,Osaka,530-0001,Japan</p>
      <p>Tel : +81-6-1234-5678　Fax : +81-6-1234-5679</p>
      <p>e-mail : info@sakurai-dc.example</p>
    </address>
    <div class="band"></div>
  </section>

</body>
</html>
```